Startup company business card (Media & Advertising)

we need a business card design for a company that is a startup in the media and aggregation industry. Card needs to look funky and of a new breed/modern and upmarket.

Target Market(s)

advertisers/ brand agencies & media publishers

Industry/Entity Type

Advertising

Contact Information for Business Card

Please ensure the front face signifies our brand (plumvexo.com) and back has details for the contact. Standard contact such as phone , address, email , website etc.

Font styles to use
Other font styles liked:
• use styleguide and logo font and color

Colors

Designer to choose colors to be used in the design.

Requirements
Must have
• We are disrupting the media and agency industry so subtlety would be good to use imagery to signify this
Nice to have
• Please use logo colors for branding
Should not have
• be as creative and provide few options. Pick a brand color from logo and styleguide

```html
<!DOCTYPE html>
<html lang="en">
<head>
<meta charset="utf-8">
<title>plumvexo business card</title>
<link rel="stylesheet" href="https://fonts.googleapis.com/css2?family=Open+Sans:wght@400;600;700;800&display=swap">
<style>
  :root {
    --backdrop: #d4d4d4;
    --ink: #0a0a0c;
    --paper: #ffffff;
    --brand-red: #ee3744;
    --text-grey: #3c3c3c;
    --shadow: rgba(0, 0, 0, 0.22);
  }
  * { margin: 0; padding: 0; box-sizing: border-box; }
  html, body {
    width: 1200px; height: 900px; overflow: hidden;
    background: var(--backdrop);
    font-family: "Open Sans", Arial, sans-serif;
  }
  .stage {
    width: 1200px; height: 900px;
    display: flex; flex-direction: column; align-items: center;
    justify-content: center; gap: 24px;
  }
  .card {
    width: 700px; height: 400px;
    position: relative; overflow: hidden;
    box-shadow: 0 4px 14px var(--shadow);
  }
  .card--front { background: var(--ink); }
  .card--back { background: var(--paper); }

  .wordmark {
    display: flex; align-items: center; gap: 16px;
    font-weight: 800; letter-spacing: -0.5px;
  }
  .wordmark__dot {
    border-radius: 50%; background: var(--brand-red); flex: none;
  }
  .card--front .wordmark {
    position: absolute; right: 70px; top: 50%; transform: translateY(-50%);
    color: var(--paper); font-size: 64px;
  }
  .card--front .wordmark__dot { width: 46px; height: 46px; }

  .card--back .wordmark {
    position: absolute; left: 70px; top: 50%; transform: translateY(-50%);
    color: var(--ink); font-size: 42px;
  }
  .card--back .wordmark__dot { width: 34px; height: 34px; }

  .divider {
    position: absolute; left: 380px; top: 120px;
    width: 2px; height: 160px; background: var(--brand-red);
  }
  .contact {
    position: absolute; left: 418px; top: 112px;
  }
  .contact__name {
    color: var(--brand-red); font-weight: 700; font-size: 24px; line-height: 1.1;
  }
  .contact__role {
    color: var(--text-grey); font-size: 16px; margin-top: 4px;
  }
  .contact__list {
    list-style: none; margin-top: 22px;
    color: var(--text-grey); font-size: 15px; line-height: 1.7;
  }
  .contact__list li { display: flex; align-items: center; gap: 10px; }
  .contact__icon { width: 14px; height: 14px; flex: none; }
</style>
</head>
<body>
<main class="stage">
  <section class="card card--front" aria-label="Card front">
    <div class="wordmark"><span class="wordmark__dot"></span><span>plumvexo</span></div>
  </section>

  <section class="card card--back" aria-label="Card back">
    <div class="wordmark"><span class="wordmark__dot"></span><span>plumvexo</span></div>
    <div class="divider"></div>
    <div class="contact">
      <p class="contact__name">Daniel Harper</p>
      <p class="contact__role">Founder</p>
      <ul class="contact__list">
        <li>
          <svg class="contact__icon" viewBox="0 0 24 24" aria-hidden="true"><path fill="#ee3744" d="M6.6 10.8a15.1 15.1 0 0 0 6.6 6.6l2.2-2.2a1 1 0 0 1 1-.25 11.4 11.4 0 0 0 3.6.57 1 1 0 0 1 1 1V20a1 1 0 0 1-1 1A17 17 0 0 1 3 4a1 1 0 0 1 1-1h3.5a1 1 0 0 1 1 1c0 1.25.2 2.45.57 3.57a1 1 0 0 1-.25 1z"/></svg>
          +61 7 5550 0142
        </li>
        <li>
          <svg class="contact__icon" viewBox="0 0 24 24" aria-hidden="true"><rect x="2.5" y="5" width="19" height="14" fill="none" stroke="#ee3744" stroke-width="2"/><path d="M2.5 5l9.5 8 9.5-8M2.5 19l7-7M21.5 19l-7-7" fill="none" stroke="#ee3744" stroke-width="2"/></svg>
          daniel@plumvexo.com
        </li>
        <li>
          <svg class="contact__icon" viewBox="0 0 24 24" aria-hidden="true"><circle cx="12" cy="12" r="9.5" fill="none" stroke="#ee3744" stroke-width="2"/><path d="M2.5 12h19M12 2.5c3 3 3 16 0 19M12 2.5c-3 3-3 16 0 19" fill="none" stroke="#ee3744" stroke-width="1.6"/></svg>
          www.plumvexo.com
        </li>
      </ul>
    </div>
  </section>
</main>
</body>
</html>
```